Fresh and Modern Real Estate Land Website

This Real Estate Agent sells only land.
The wordpress design will need to work well with responsive Avada theme.
Colors should complement the attached Home-Header.jpg, the Sonoran Desert, Southwest Region of Arizona and Tucson.
Home page layout to include
- Logo Attached: NewLogo.png
- Agent Photo: MaeDorn.jpg
- Contact Detials: use Phone
- Slogan: "I've Never Shown a House"
- Static header or Main image (see Attached Home-Header.jpg) - The dimensions of this shot may not be correct for your design. Please select from similar stock if needed and provide stock photo id.
- Intro/Welcome Text See Attached: Intro.txt
- Vertical or Horizontal display of "New" listings (include: Photo, Price, exerpt/intro) see: Properties.zip
- Tools of the trade. Home page will have a section called "Tools Of the Trade" These are items the agent uses in her work. This seciton will need to be 3 or More Images about 100 characters of text and Title. These will rotate through about 12 different tools. see: tools-of-the-trade.zip
Footer to include Contact Info/Recent Blog Posts/Testimonial
No Social Network icons
Main Menu:
Home
Properties
Testimonials
Services
About Mae
Blog
Contact
- Marck Script google/Times new Roman is logo. Designers Choice.

```html
<!DOCTYPE html>
<html lang="en">
<head>
<meta charset="utf-8">
<title>Mae Dorn – Land Lady</title>
<link href="https://fonts.googleapis.com/css2?family=Open+Sans:wght@400;600;700&family=Marck+Script&display=swap" rel="stylesheet">
<style>
:root{
  --orange:#f07b2e;
  --orange-light:#f5a04a;
  --orange-dark:#e8691f;
  --ink:#2b1a10;
  --text:#444;
  --white:#fff;
  --footer:#2b2627;
  --footer-bottom:#231f20;
  --footer-text:#e6e6e6;
  --border:#c9c9c9;
}
*{margin:0;padding:0;box-sizing:border-box}
html,body{width:875px;height:1200px;overflow:hidden;background:var(--white)}
body{position:relative;font-family:"Open Sans",Arial,sans-serif;color:var(--text)}
.abs{position:absolute}

/* header */
.site-header{position:absolute;left:0;top:0;width:875px;height:61px;background:var(--white)}
.brand{left:133px;top:18px;font-size:22px;font-weight:700;color:var(--orange);letter-spacing:.3px;line-height:1}
.slogan{left:284px;top:31px;font-family:"Marck Script",cursive;font-size:15px;color:#444;line-height:1}
.call{left:619px;top:25px;display:flex;align-items:center;gap:5px}
.call-label{font-size:6.5px;font-weight:700;color:#333;line-height:1}
.call-number{font-size:16px;font-weight:700;color:var(--orange);line-height:1.05}

/* nav */
.main-nav{position:absolute;left:0;top:61px;width:875px;height:27px;background:var(--orange);box-shadow:0 2px 3px rgba(0,0,0,.25);z-index:2}
.main-nav a{position:absolute;top:9px;font-size:7.3px;font-weight:700;color:var(--white);text-decoration:none;letter-spacing:.2px;line-height:1}
.main-nav a.active{color:#3a2a1a}

/* hero */
.hero{left:0;top:88px;width:875px;height:292px;
  background:linear-gradient(180deg,#7fa6d6 0%,#c9d8ea 30%,#e9ebee 45%,#8b8f6c 55%,#9d8f5a 72%,#b7a272 100%)}

/* welcome */
.welcome{left:0;top:380px;width:875px;height:136px;background:linear-gradient(180deg,var(--orange-dark),#f28a3a)}
.welcome-notch{left:418px;top:515px}
.agent-photo{left:133px;top:16px;width:73px;height:98px;border:2px solid var(--white);background:linear-gradient(180deg,#b9c6d6,#d8a894 55%,#d8262c 80%)}
.welcome-title{left:216px;top:15px;font-size:15.5px;font-weight:700;color:var(--ink);line-height:1.2}
.welcome-title span{color:var(--white)}
.welcome-text{left:216px;width:518px;font-size:9px;line-height:11.5px;color:#3a2212}

/* listings */
.listing{width:189px;height:206px;top:556px;border:1px solid var(--border);background:var(--white)}
.listing h2{position:absolute;top:7px;width:100%;text-align:center;font-size:12px;font-weight:700;color:#222;letter-spacing:.3px}
.listing .photo{position:absolute;left:9px;top:28px;width:169px;height:138px}
.listing .price{position:absolute;left:9px;top:142px;width:169px;height:24px;background:rgba(20,20,20,.85);color:var(--white);font-size:12px;font-weight:700;padding:4px 9px}
.listing p{position:absolute;left:9px;top:172px;width:150px;font-size:7.2px;line-height:12.5px;color:#444}

/* tools */
.tools-band{left:0;top:793px;width:875px;height:217px;background:linear-gradient(180deg,var(--orange-dark),var(--orange-light))}
.tools-panel{left:133px;top:793px;width:608px;height:217px;background:var(--white)}
.tool{top:810px;width:179px}
.tool .photo{width:179px;height:138px;border:1px solid var(--border)}
.tool h3{text-align:center;font-size:12.5px;font-weight:700;color:#222;margin-top:5px;letter-spacing:.3px}
.tool p{text-align:center;font-size:7.3px;line-height:12.5px;color:#444;padding:0 20px}
.arrow{top:883px}

/* footer */
.site-footer{left:0;top:1010px;width:875px;height:162px;background:var(--footer)}
.footer-heading{top:1032px;font-size:10px;font-weight:600;color:var(--orange)}
.f-text{font-family:Arial,Helvetica,sans-serif;font-size:7px;line-height:12.5px;color:var(--footer-text)}
.blog-list{list-style:none}
.blog-list li{height:15.6px}
.footer-brand{left:133px;top:1118px;font-size:22px;font-weight:700;color:var(--orange)}
.footer-bottom{left:0;top:1172px;width:875px;height:28px;background:var(--footer-bottom);border-top:1px solid #3a3536}
.copyright{width:100%;text-align:center;top:9px;font-family:Arial,Helvetica,sans-serif;font-size:7px;color:var(--footer-text)}
.copyright span{color:var(--orange)}
</style>
</head>
<body>

<header class="site-header">
  <div class="abs brand">Mae Dorn</div>
  <div class="abs slogan">I've Never Shown a House</div>
  <div class="abs call">
    <svg width="21" height="21" viewBox="0 0 21 21"><circle cx="10.5" cy="10.5" r="9.3" fill="none" stroke="#f07b2e" stroke-width="1.6"/><path d="M7.4 5.6l1.8-.3 1 2.5-1.2.9c.5 1.3 1.4 2.3 2.6 2.9l1-1.1 2.4 1.1-.3 1.8c-3.9.5-7.8-3.5-7.3-7.8z" fill="#333"/></svg>
    <div><div class="call-label">CALL ON US</div><div class="call-number">000 000 0000</div></div>
  </div>
</header>

<nav class="main-nav">
  <a class="active" style="left:131px">HOME</a>
  <a style="left:182px">PROPERTIES</a>
  <a style="left:254px">TESTIMONIALS</a>
  <a style="left:335px">SERVICES</a>
  <a style="left:397px">ABOUT MAE</a>
  <a style="left:466px">BLOG</a>
  <a style="left:514px">CONTACT</a>
</nav>

<div class="abs hero" role="img" aria-label="Sonoran desert road with a tall saguaro cactus under a cloudy blue sky"></div>

<section class="abs welcome">
  <div class="abs agent-photo" role="img" aria-label="Portrait photo of agent Mae Dorn"></div>
  <h1 class="abs welcome-title">Welcome to the <span>Land Lady</span></h1>
  <p class="abs welcome-text" style="top:44px">When you are looking for Tucson land, Mae Dorn's experience has "landed" her among the top 1/2% ranking of all Realtors, and that's just selling LAND!</p>
  <p class="abs welcome-text" style="top:78px">Mae is proud to say that she STILL has never sold a house... but she does know the best who do.&nbsp; 90% of real estate is sold by 10% of the Realtors and, during nearly 30 years of selling, Mae knows and is good friends with these 10%. Utilize Mae's contacts so she can match up the right home agent...for YOU!</p>
</section>
<svg class="abs welcome-notch" width="40" height="22" viewBox="0 0 40 22"><path d="M0 0H40L20 22Z" fill="#f28a3a"/><path d="M15 6l5 5 5-5" fill="none" stroke="#fff" stroke-width="2"/></svg>

<article class="abs listing" style="left:133px">
  <h2>AVE SHELLY</h2>
  <div class="photo" role="img" aria-label="Golden desert sunset over land parcel" style="background:linear-gradient(180deg,#d98a0c,#f4c21a 45%,#e9a412 70%,#3a2506)"></div>
  <div class="price">$200</div>
  <p>Lorem Ipsum is simply dummy text of the printing and typesetting industry.</p>
</article>
<article class="abs listing" style="left:342px">
  <h2>RED MOUNTAIN</h2>
  <div class="photo" role="img" aria-label="Desert lot with green scrub and mountains" style="background:linear-gradient(180deg,#8fb0d8,#b7c3cc 25%,#7d8a6a 35%,#5f7a48 60%,#a4a58a)"></div>
  <div class="price">$200</div>
  <p>Lorem Ipsum is simply dummy text of the printing and typesetting industry.</p>
</article>
<article class="abs listing" style="left:552px">
  <h2>TURTLE</h2>
  <div class="photo" role="img" aria-label="Desert land with saguaros and mountains under blue sky" style="background:linear-gradient(180deg,#2e6cc4,#7aa6e0 30%,#8a8a7a 40%,#5a6a3a 60%,#8a8060)"></div>
  <div class="price">$200</div>
  <p>Lorem Ipsum is simply dummy text of the printing and typesetting industry.</p>
</article>

<div class="abs tools-band"></div>
<div class="abs tools-panel"></div>
<svg class="abs arrow" style="left:113px" width="20" height="36" viewBox="0 0 20 36"><path d="M20 0V36L0 18Z" fill="#2b2627"/><path d="M12 13l-5 5 5 5" fill="none" stroke="#fff" stroke-width="2"/></svg>
<svg class="abs arrow" style="left:741px" width="20" height="36" viewBox="0 0 20 36"><path d="M0 0V36L20 18Z" fill="#2b2627"/><path d="M8 13l5 5-5 5" fill="none" stroke="#fff" stroke-width="2"/></svg>

<div class="abs tool" style="left:148px">
  <div class="photo" role="img" aria-label="Yellow long tape measure" style="background:radial-gradient(circle at 45% 50%,#f3c915 0,#e8b80c 30%,#f4f4f4 55%)"></div>
  <h3>TAPE-MEASURE</h3>
  <p>Lorem Ipsum is simply dummy text of the printing and typesetting industry.</p>
</div>
<div class="abs tool" style="left:348px">
  <div class="photo" role="img" aria-label="Field compass with leather pouch" style="background:radial-gradient(circle at 50% 50%,#4a3a2e 0,#6b5a48 30%,#f4f4f4 58%)"></div>
  <h3>COMPAS</h3>
  <p>Lorem Ipsum is simply dummy text of the printing and typesetting industry.</p>
</div>
<div class="abs tool" style="left:547px">
  <div class="photo" role="img" aria-label="Roll of orange flagging tape" style="background:radial-gradient(circle at 55% 50%,#ff4a1a 0,#ff5a22 28%,#f6f6f6 56%)"></div>
  <h3>ORANGE TAPE</h3>
  <p>Lorem Ipsum is simply dummy text of the printing and typesetting industry.</p>
</div>

<footer class="abs site-footer"></footer>
<h4 class="abs footer-heading" style="left:133px">Contact Info</h4>
<h4 class="abs footer-heading" style="left:386px">Recent Blog Posts</h4>
<h4 class="abs footer-heading" style="left:556px">Testimonial</h4>

<div class="abs f-text" style="left:133px;top:1052px;width:185px">
  <svg width="8" height="8" viewBox="0 0 8 8" style="vertical-align:-1px"><path d="M4 0L8 4H7V8H1V4H0Z" fill="#f07b2e"/></svg>
  Lorem Ipsum is simply dummy text of the printing and typesetting industry.
</div>
<div class="abs f-text" style="left:133px;top:1084px;display:flex;align-items:center;gap:4px">
  <svg width="12" height="8" viewBox="0 0 12 8"><path d="M1 3C3 0 9 0 11 3L9 4 8 2H4L3 4Z M3 4H9L10 8H2Z" fill="#f07b2e"/></svg>
  <span>(+00) 000 12345</span>
  <svg width="11" height="8" viewBox="0 0 11 8" style="margin-left:8px"><rect width="11" height="8" fill="#f07b2e"/><path d="M0 0L5.5 4.5 11 0" fill="none" stroke="#2b2627" stroke-width="1"/></svg>
  <span>mail@example.com</span>
</div>
<div class="abs footer-brand">Mae Dorn</div>

<ul class="abs blog-list f-text" style="left:387px;top:1051px">
  <li>Blog Slideshow Post</li>
  <li>Aenean Odio Mauris</li>
  <li>Blog Image Post</li>
  <li>Blog Video Post</li>
  <li>Donec Suscipit Dim Euismods</li>
</ul>

<p class="abs f-text" style="left:558px;top:1050px;width:170px">Mae is proud to say that she STILL has never sold a house... but she does know the best who do.&nbsp; 90% of real estate is sold by 10% of the Realtors and, during nearly 30 years of selling, Mae knows and is good friends with these 10%. Utilize Mae's contacts so she can match up the right home agent...for YOU!</p>

<div class="abs footer-bottom">
  <div class="abs copyright">© 2014 <span>Mae Dorn</span>, All Rights Reserved</div>
</div>

</body>
</html>
```